Website for a Psychologist in Private Practice

I need a cool web design for my website: www.drquorvat.com. I would like it to look professional. Keep all the current content and add: Space for video; radio spots (see Velvet Tide Hour Logo below for those); Quick Inquiry; Brindlepost link; 5 star rating on Zunq; a map; reviews from former patients. I am open to suggestions.

Target Market(s)

Those seeking individual and marital counseling.

Industry/Entity Type

Mental Health

Number of Pages Required

1 page

Font styles to use
Sans Serif
Other font styles liked:
• I'm open but no hard to read script

Requirements
Must have
• All the content on my home page with link for video and radio spots. List services and degrees and expertices (pics not necessary).
Nice to have
• A video of me and radio conversations (logo of Velvet Tide Hour radio attached).
Should not have
• Cartoons, comedy, etc.... I don't need pictures of services (marital, depression, etc...) Just list those.

```html
<!DOCTYPE html>
<html lang="en">
<head>
<meta charset="utf-8">
<title>Dr. Marla J. Quorvat — Psychologist</title>
<link href="https://fonts.googleapis.com/css2?family=Raleway:wght@500;600;700;800&family=Lato:wght@400;700&display=swap" rel="stylesheet">
<style>
:root{
  --blue:#2a7dc0;
  --gold:#c8ab55;
  --tan:#d0c18c;
  --dark:#262626;
  --darker:#1a1a1a;
  --black:#060606;
  --light:#f1f1f1;
  --text:#444;
  --white:#fff;
}
*{box-sizing:border-box;margin:0;padding:0}
html,body{width:1200px;height:3082px;overflow:hidden}
body{font-family:"Lato",sans-serif;color:var(--text);background:var(--white);position:relative}
.abs{position:absolute}
h2{font-family:"Raleway",sans-serif;font-weight:700;font-size:31px;color:#222;letter-spacing:.3px}
h2 span{color:var(--blue)}
.rule{width:36px;height:3px;background:var(--blue);margin-top:14px}

/* top bar */
.topbar{left:0;top:0;width:1200px;height:42px;background:var(--dark);color:#ddd;font-size:12px;font-weight:700}
.topbar .item{position:absolute;top:13px;display:flex;align-items:center;gap:8px}
.topbar .social{position:absolute;top:0;height:42px;width:27px;border-left:1px solid #3a3a3a;display:flex;align-items:center;justify-content:center}
.topbar .social i{width:10px;height:10px;border-radius:50%;background:var(--gold)}

/* header */
.header{left:0;top:42px;width:1200px;height:94px;background:#fafafa}
.brand{position:absolute;left:100px;top:26px;font-family:"Raleway",sans-serif;font-weight:600;font-size:34px;color:var(--gold)}
.nav{position:absolute;top:28px;left:557px;display:flex;align-items:center;font-family:"Raleway",sans-serif;font-weight:700;font-size:13.5px;color:#222}
.nav a{color:inherit;text-decoration:none;padding:12px 11px}
.nav a.active{background:var(--blue);color:#fff;border-radius:2px;padding:12px 14px;margin-right:9px}

/* hero */
.hero{left:0;top:136px;width:1200px;height:462px;background:linear-gradient(135deg,#6d7a3c 0%,#9aa65a 40%,#7f8c45 70%,#4d5a2a 100%)}
.hero .caption{position:absolute;left:0;bottom:0;width:1200px;height:48px;background:rgba(30,30,30,.55);color:#fff;font-family:"Raleway",sans-serif;font-weight:600;font-size:27px;text-align:center;line-height:48px}
.hero .arrow{position:absolute;top:200px;width:36px;height:30px;background:rgba(20,20,20,.7);display:flex;align-items:center;justify-content:center}

/* about */
.about-photo{left:0;top:598px;width:600px;height:485px;background:linear-gradient(160deg,#5e7a3a 0%,#c9b48a 45%,#3a5a8a 100%)}
.about{left:600px;top:598px;width:600px;height:485px;background:var(--light);padding:40px 39px 0}
.about h2{font-size:30px}
.about h2 span{color:var(--gold)}
.about p{font-size:13.2px;line-height:22px;color:#555;margin-top:14px;width:500px}
.about h4{font-family:"Raleway",sans-serif;font-weight:700;color:var(--blue);font-size:15px;margin-top:18px}
.about ul{list-style:none;font-size:12.5px;line-height:23px;color:#555;margin-top:8px}
.btn{display:inline-block;background:var(--blue);color:#fff;font-family:"Raleway",sans-serif;font-weight:700;font-size:13px;text-align:center;border-radius:2px}
.about .btn{margin-top:18px;width:115px;height:40px;line-height:40px}

/* expertise */
.expertise{left:0;top:1083px;width:1200px;height:697px;background:var(--tan)}
.expertise h2{position:absolute;left:0;width:1145px;text-align:center;top:34px;font-size:31px}
.expertise .rule{position:absolute;left:553px;top:84px;margin:0}
.exp-label{position:absolute;width:300px}
.exp-label h5{font-family:"Raleway",sans-serif;font-weight:700;font-size:16px;color:var(--blue)}
.exp-label p{font-size:11.8px;color:#333;line-height:15px;margin-top:4px}
.exp-label.left{text-align:right}
.hub-name{position:absolute;left:505px;top:330px;width:140px;text-align:center;font-family:"Raleway",sans-serif;font-weight:600;font-size:19px;color:var(--gold);line-height:24px}

/* media */
.media{left:0;top:1780px;width:1200px;height:520px;background:var(--black);color:#ddd}
.media h2{color:#fff;font-size:30px}
.radio{position:absolute;left:100px;top:58px;width:460px}
.quote{margin-top:46px;font-size:14.5px;line-height:25px;color:#ddd}
.quote .mark{color:var(--gold);font-family:"Raleway",sans-serif;font-weight:800;font-size:22px}
.speaker{color:var(--gold);font-weight:700;font-size:15.5px;margin-top:16px}
.radio .btn{margin-top:66px;width:111px;height:39px;line-height:39px}
.video-head{position:absolute;left:616px;top:58px}
.video{position:absolute;left:616px;top:148px;width:584px;height:306px;background:linear-gradient(120deg,#c9bfae 0%,#8a9a8c 45%,#d7cec0 100%)}

/* sessions */
.sessions-wrap{left:0;top:2300px;width:1200px;height:454px;background:var(--white)}
.form{position:absolute;left:99px;top:39px;width:326px;height:404px;border:6px solid #e6e6e6;padding:28px 33px 0;text-align:center}
.form h3{font-family:"Raleway",sans-serif;font-weight:700;color:var(--blue);font-size:16px}
.field{height:33px;border:1px solid #d6d6d6;border-radius:2px;font-size:11.5px;color:#777;text-align:left;padding:0 10px;line-height:31px;position:relative;margin-top:18px}
.form .first{margin-top:30px}
.field .caret{position:absolute;right:0;top:0;width:26px;height:31px;border-left:1px solid #d6d6d6;display:flex;align-items:center;justify-content:center}
.row{display:flex;gap:20px}
.row .field{flex:1}
.form .btn{margin-top:20px;width:92px;height:37px;line-height:37px;font-size:14px}
.sessions{position:absolute;left:483px;top:58px;width:620px}
.sessions ul{list-style:none;margin-top:22px}
.sessions li{position:relative;padding-left:28px;font-size:13.4px;font-weight:700;color:#333;line-height:18px;margin-bottom:14px}
.sessions li svg{position:absolute;left:0;top:1px}

/* footer */
.footer{left:0;top:2754px;width:1200px;height:283px;background:var(--dark);color:#ccc}
.footer h4{font-family:"Raleway",sans-serif;font-weight:700;font-size:18px;color:#fff}
.footer h4 span{color:var(--blue)}
.col{position:absolute;top:37px}
.links{list-style:none;margin-top:14px;font-size:12.5px;line-height:30px}
.links li:before{content:"";display:inline-block;width:4px;height:4px;border-radius:50%;background:#ccc;margin:0 8px 3px 0}
.links li.active{color:var(--gold)}
.contact{font-size:12.5px;line-height:19px}
.contact .c{display:flex;gap:12px;margin-top:14px}
.contact b{color:#fff}
.map{position:absolute;left:577px;top:74px;width:282px;height:115px;background:linear-gradient(135deg,#e4e1d8 0%,#d3d7cd 50%,#e9e6de 100%);border:3px solid #fff}
.follow .dots{display:flex;gap:11px;margin-top:22px}
.follow .dots i{width:36px;height:36px;border-radius:50%;background:var(--blue)}
.follow p{font-size:12px;font-weight:700;color:#fff;margin-top:28px;line-height:16px}
.follow .badges{display:flex;gap:12px;margin-top:14px}
.follow .badges i{width:78px;height:36px;background:#f4f4f4;border-radius:2px}
.copy{left:0;top:3037px;width:1200px;height:45px;background:var(--darker);color:#ccc;font-size:12.5px;text-align:center;line-height:45px}
</style>
</head>
<body>

<div class="abs topbar">
  <div class="item" style="left:100px">
    <svg width="14" height="10" viewBox="0 0 14 10"><rect x="0.5" y="0.5" width="13" height="9" fill="none" stroke="#c8ab55"/><path d="M1 1l6 5 6-5" fill="none" stroke="#c8ab55"/></svg>
    mq@drquorvat.com
  </div>
  <div class="item" style="left:249px">
    <svg width="12" height="12" viewBox="0 0 12 12"><path d="M2 1l2.5 0 1 3-1.5 1c.7 1.5 1.6 2.4 3 3l1-1.5 3 1v2.5c-5 0-9-4-9-9z" fill="#c8ab55"/></svg>
    (949) 555 0182
  </div>
  <div class="social" style="left:1050px" aria-label="Brindlepost"><i></i></div>
  <div class="social" style="left:1077px;border-right:1px solid #3a3a3a" aria-label="Chirpline"><i></i></div>
</div>

<header class="abs header">
  <div class="brand">Dr. Marla J. Quorvat</div>
  <nav class="nav">
    <a class="active">HOME</a><a>SESSIONS</a><a>MY EXPERTISE</a><a>RESOURCES</a><a>BIO</a><a>CONTACT US</a>
  </nav>
</header>

<section class="abs hero" role="img" aria-label="Photo of a woman with arms spread wide in a sunny green park">
  <div class="arrow" style="left:4px"><svg width="10" height="12" viewBox="0 0 10 12"><path d="M8 1L2 6l6 5z" fill="#fff"/></svg></div>
  <div class="arrow" style="right:4px"><svg width="10" height="12" viewBox="0 0 10 12"><path d="M2 1l6 5-6 5z" fill="#fff"/></svg></div>
  <div class="caption">I am a psychologist providing individual and marital counseling</div>
</section>

<div class="abs about-photo" role="img" aria-label="Portrait of the psychologist outdoors in a blue blouse"></div>
<section class="abs about">
  <h2>ABOUT <span>DR. MARLA J. QUORVAT</span></h2>
  <div class="rule"></div>
  <p>While I acknowledge the importance of my education, I also appreciate the role my experiences have played in allowing me to relate so well to others. Allow me to share those I feel are most relevant with you.</p>
  <p style="margin-top:8px">I survived an abusive childhood that my mother and sister unfortunately did not.&nbsp; And it was my grief and desire to become stronger than my past that led me to counseling. A process that clearly changed my life</p>
  <h4>MY DEGREES</h4>
  <ul>
    <li>Doctoral Degree in Clinical Psychology</li>
    <li>Masters Degree in Counseling Psychology</li>
    <li>Doctoral Internship, Coastline Medical Center</li>
    <li>Masters Internship, Ridgeway Clinic</li>
  </ul>
  <span class="btn">READ MORE</span>
</section>

<section class="abs expertise">
  <h2>MY <span>EXPERTISE</span></h2>
  <div class="rule"></div>
  <svg class="abs" style="left:0;top:0" width="1200" height="697" viewBox="0 0 1200 697">
    <g stroke="#9d8a55" stroke-width="1.5" fill="none">
      <line x1="571" y1="378" x2="569" y2="195"/><line x1="571" y1="378" x2="707" y2="277"/>
      <line x1="571" y1="378" x2="707" y2="479"/><line x1="571" y1="378" x2="569" y2="577"/>
      <line x1="571" y1="378" x2="432" y2="479"/><line x1="571" y1="378" x2="432" y2="277"/>
    </g>
    <g stroke="#2a7dc0" stroke-width="1" fill="none">
      <polyline points="414,150 455,150 520,170"/>
      <polyline points="869,274 800,274 760,290"/>
      <polyline points="874,461 800,461 760,475"/>
      <polyline points="736,612 640,612 600,600"/>
      <polyline points="278,499 350,499 380,490"/>
      <polyline points="266,277 335,277 378,285"/>
    </g>
    <g fill="#2a7dc0">
      <circle cx="414" cy="150" r="2.5"/><circle cx="869" cy="274" r="2.5"/><circle cx="874" cy="461" r="2.5"/>
      <circle cx="736" cy="612" r="2.5"/><circle cx="278" cy="499" r="2.5"/><circle cx="266" cy="277" r="2.5"/>
    </g>
    <g fill="#c4a448" stroke="#f3ebcf" stroke-width="6">
      <circle cx="569" cy="195" r="52"/><circle cx="707" cy="277" r="52"/><circle cx="707" cy="479" r="52"/>
      <circle cx="569" cy="577" r="52"/><circle cx="432" cy="479" r="52"/><circle cx="432" cy="277" r="52"/>
    </g>
    <g fill="none" stroke="#fff" stroke-width="1.5" opacity=".6">
      <circle cx="569" cy="195" r="40"/><circle cx="707" cy="277" r="40"/><circle cx="707" cy="479" r="40"/>
      <circle cx="569" cy="577" r="40"/><circle cx="432" cy="479" r="40"/><circle cx="432" cy="277" r="40"/>
    </g>
    <circle cx="571" cy="378" r="72" fill="#1f5f9a" stroke="#fff" stroke-width="7"/>
  </svg>
  <div class="hub-name">Dr. Marla J.<br>Quorvat</div>

  <div class="exp-label left" style="left:110px;top:136px"><h5>Dating</h5><p>Lorem ipsum dolor sit amensectetuer<br>adipiscing elit, seddiam no</p></div>
  <div class="exp-label" style="left:876px;top:258px"><h5>Marriage</h5><p>Lorem ipsum dolor sit amensectetuer<br>adipiscing elit, seddiam no</p></div>
  <div class="exp-label" style="left:880px;top:442px"><h5>Parenting &amp; Professional<br>Relationships</h5><p>Lorem ipsum dolor sit amensectetuer<br>adipiscing elit, seddiam no</p></div>
  <div class="exp-label" style="left:742px;top:597px"><h5>Depression &amp; Anxiety Issues</h5><p>Lorem ipsum dolor sit amensectetuer<br>adipiscing elit, seddiam no</p></div>
  <div class="exp-label left" style="left:-27px;top:481px"><h5>Personality Disorders</h5><p>Lorem ipsum dolor sit<br>amensectetuer adipiscing elit,</p></div>
  <div class="exp-label left" style="left:-39px;top:260px"><h5>Life Management</h5><p>Lorem ipsum dolor sit<br>amensectetuer adipiscing elit,</p></div>
</section>

<section class="abs media">
  <div class="radio">
    <h2>RADIO <span>CONVERSATIONS</span></h2>
    <p class="quote"><span class="mark">“</span> Lorem ipsum dolor sit amet, consectetuer adipiscing elit, sed diam nonummy tincidunt ut laoreet dolore magna quam erat volutpat. Ut wisi enim ad minim veniam, quis nostrud exerci tation ullamcorper suscipit lobortis nisl ut aliquip ex ea commodo consequat. Duis autem vel eum iriure.laoreet dolore magna quam erat <span class="mark">”</span></p>
    <div class="speaker">Owen Marsh</div>
    <span class="btn">VIEW ALL</span>
  </div>
  <h2 class="video-head">VIEW <span>VIDEO</span></h2>
  <div class="video" role="img" aria-label="Video still of a counseling session with a family in a bright room">
    <svg class="abs" style="left:262px;top:123px" width="60" height="60" viewBox="0 0 60 60"><circle cx="30" cy="30" r="26" fill="rgba(0,0,0,.25)" stroke="#fff" stroke-width="3"/><path d="M24 18l16 12-16 12z" fill="#fff"/></svg>
  </div>
</section>

<section class="abs sessions-wrap">
  <div class="form">
    <h3>SCHEDULE AN APPOINTMENT</h3>
    <div class="field first">Full Name</div>
    <div class="field">Phone Number</div>
    <div class="row">
      <div class="field">Date<span class="caret"><svg width="8" height="5" viewBox="0 0 8 5"><path d="M0 0h8L4 5z" fill="#c8ab55"/></svg></span></div>
      <div class="field">Time<span class="caret"><svg width="8" height="5" viewBox="0 0 8 5"><path d="M0 0h8L4 5z" fill="#c8ab55"/></svg></span></div>
    </div>
    <div class="field">Location<span class="caret"><svg width="8" height="5" viewBox="0 0 8 5"><path d="M0 0h8L4 5z" fill="#c8ab55"/></svg></span></div>
    <span class="btn">SUBMIT</span>
  </div>
  <div class="sessions">
    <h2>MY <span>SESSIONS</span></h2>
    <div class="rule"></div>
    <ul>
      <li><svg width="16" height="14" viewBox="0 0 16 14"><path d="M1 7l5 5L15 1" fill="none" stroke="#2a7dc0" stroke-width="2.5"/></svg>Individual sessions are 50 minutes in length</li>
      <li><svg width="16" height="14" viewBox="0 0 16 14"><path d="M1 7l5 5L15 1" fill="none" stroke="#2a7dc0" stroke-width="2.5"/></svg>Marriage sessions are typically 50 to 75 minutes in length</li>
      <li><svg width="16" height="14" viewBox="0 0 16 14"><path d="M1 7l5 5L15 1" fill="none" stroke="#2a7dc0" stroke-width="2.5"/></svg>Family sessions are 60 to 75 minutes in length</li>
      <li><svg width="16" height="14" viewBox="0 0 16 14"><path d="M1 7l5 5L15 1" fill="none" stroke="#2a7dc0" stroke-width="2.5"/></svg>Divorce Mediation sessions are primarily conducted with individual sessions for each spouse with meetings as a couple kept to a minimum</li>
      <li><svg width="16" height="14" viewBox="0 0 16 14"><path d="M1 7l5 5L15 1" fill="none" stroke="#2a7dc0" stroke-width="2.5"/></svg>Custody Evaluation sessions are usually initiated by each parties attorneys or the presiding judge</li>
      <li><svg width="16" height="14" viewBox="0 0 16 14"><path d="M1 7l5 5L15 1" fill="none" stroke="#2a7dc0" stroke-width="2.5"/></svg>Testing sessions vary in length dependent upon the nature of the psychological assessment needed</li>
    </ul>
  </div>
</section>

<footer class="abs footer">
  <div class="col" style="left:100px">
    <h4>Quick <span>Links</span></h4>
    <ul class="links">
      <li class="active">Home</li><li>Sessions</li><li>My Expertise</li><li>Resources</li><li>Bio</li><li>Contact Us</li>
    </ul>
  </div>
  <div class="col contact" style="left:288px">
    <h4>Contact <span>Details</span></h4>
    <div class="c"><svg width="12" height="16" viewBox="0 0 12 16"><path d="M6 0a6 6 0 0 0-6 6c0 4.5 6 10 6 10s6-5.5 6-10a6 6 0 0 0-6-6zm0 8.5A2.5 2.5 0 1 1 6 3.5a2.5 2.5 0 0 1 0 5z" fill="#fff"/></svg><div><b>Dr. Marla J. Quorvat</b><br>450 Linden Court #212<br>Harbor Vale, CA 92601</div></div>
    <div class="c" style="margin-top:22px"><svg width="12" height="12" viewBox="0 0 12 12"><path d="M2 1l2.5 0 1 3-1.5 1c.7 1.5 1.6 2.4 3 3l1-1.5 3 1v2.5c-5 0-9-4-9-9z" fill="#fff"/></svg>(949) 555 0182</div>
    <div class="c" style="margin-top:20px"><svg width="10" height="14" viewBox="0 0 10 14"><rect x="0.5" y="0.5" width="9" height="13" rx="1.5" fill="none" stroke="#fff"/><circle cx="5" cy="11" r="1" fill="#fff"/></svg>(949) 555 0182</div>
    <div class="c" style="margin-top:20px"><svg width="14" height="10" viewBox="0 0 14 10"><rect x="0.5" y="0.5" width="13" height="9" fill="none" stroke="#fff"/><path d="M1 1l6 5 6-5" fill="none" stroke="#fff"/></svg>mq@drquorvat.com</div>
  </div>
  <div class="col" style="left:577px">
    <h4>Location <span>Map</span></h4>
  </div>
  <div class="map" role="img" aria-label="Street map showing the office location"></div>
  <div class="col follow" style="left:939px">
    <h4>Follow <span>Us</span></h4>
    <div class="dots"><i aria-label="Brindlepost"></i><i aria-label="Chirpline"></i></div>
    <p>A portion of all revenue<br>is donated to</p>
    <div class="badges"><i></i><i></i></div>
  </div>
</footer>
<div class="abs copy">Copyright © 2016 Dr. Marla J. Quorvat. All Rights Reserved</div>

</body>
</html>
```